依頼詳細
今回は、トップページデザインの募集になります。
レスポンシブデザインのサイトで、bootstrap4を利用しコーディングする予定になります。
デザイン幅は2000px、コンテンツの幅はbootstrap4デフォルトの1110pxを基準としてください。ただし最近のデザインの流行を取りいれて、フルワイドや、1200~15000px程度の幅のコンテンツをバランスよくレイアウトしてください。
コンテンツ配置は基本12分割になります。がデザインによっては、多少逸脱してもかまいません。
念のため、サンプルのPSDデータを添付しますので、参照ください。

本文のフォントはゴシック系は游ゴシック、メイリオ、明朝系は遊明朝でお願いします。
飾り文字はフリーフォントか、googleフォントを利用してください。

メイン画像部分・グローバルメニューは、ワイド適用でお願いします。

資料上はサイト名(社名)や住所などは伏字にしております。ご提案時点ではそのまま作成をお願いします。当選確定後、本内容に修正をお願いいたします。

当選の方は、希望があれば引き続き下層ページの作成及びコーディング作業を依頼可能です。
不明点、質問などありましたらメッセージ等でご連絡ください。

・カラー
青系(爽やかなイメージ)

・掲載画像
必ず添付ファイルを使用してください。
また、雰囲気が合っていれば、指定外の画像を背景などに使用いただいてもOKです。

・その他
内容詳細に関しては、別添のExcel資料を参照してください。
サイトURL
ページ数
1ページ
希望イメージ
シンプル 複雑
単色 カラフル
暗い 明るい
日常 高級
遊び心 厳粛
未来的 伝統的
女性的 男性的
希望する色
青系、水色系
納品ファイル
• 高解像度JPG (.jpg)
• フォトショップ形式 (.psd)
補足説明
納品ファイルは、PDF及びクライアント表示確認用のJPGを準備お願いします。
■ 選んだ理由

今回は、贅沢さや豪華さをイメージさせる洗練された先進的なデザインを希望しており、見た目が大事な案件でした。
業界的に国内外問わず「サイトの見た目」をかなり重要視しているため、"見栄えのするデザイン"というところに重きを置いてクライアントとの折衝の結果、velbornさかた様を選定させていただきました。

■ 提案者全員のお礼・コメント

どの案も制作意図を組んでいただきとてもよかったのですが、今回はvelbornさかた様を当選とさせていただきました。
皆様ご提案ありがとうございました。
今後ともご提案宜しくお願いいたします。

```html
<!DOCTYPE html>
<html lang="ja">
<head>
<meta charset="utf-8">
<title>Safety and High Quality</title>
<link href="https://fonts.googleapis.com/css2?family=Noto+Sans+JP:wght@400;500;700&family=Noto+Serif+JP:wght@400;500&family=Parisienne&family=Cormorant+Garamond:wght@400;500&display=swap" rel="stylesheet">
<style>
  :root {
    --navy: #2c3a55;
    --navy-deep: #1d2942;
    --blue: #3d6fb3;
    --sky: #8fbbe0;
    --band: #e6edf6;
    --ink: #3a3f4a;
    --muted: #7b8290;
    --line: #c9d2de;
    --paper: #ffffff;
    --canvas: #f5f7fa;
  }
  * { margin: 0; padding: 0; box-sizing: border-box; }
  html, body { width: 801px; height: 1200px; overflow: hidden; }
  body {
    position: relative;
    background: var(--canvas);
    font-family: "Noto Sans JP", sans-serif;
    color: var(--ink);
  }
  .band { position: absolute; left: 0; top: 0; width: 801px; height: 1200px; }
  .page { position: absolute; left: 139px; top: 0; width: 521px; height: 1200px; }
  .page-bg {
    position: absolute; left: 0; top: 0; width: 521px; height: 990px;
    background: var(--paper); opacity: .55;
  }

  /* hero */
  .hero {
    position: absolute; left: 0; top: 0; width: 521px; height: 315px;
    background: linear-gradient(180deg, #6fa7d9 0%, #a9cdea 30%, #5d86a8 55%, #2f6a8a 72%, #2d5a46 88%, #3f6b4a 100%);
  }
  .nav {
    position: absolute; left: 0; top: 0; width: 521px; height: 22px;
    background: rgba(29, 41, 66, .85);
    display: flex; align-items: center; padding: 0 12px 0 38px;
  }
  .nav-brand {
    font-size: 7px; font-weight: 500; color: #fff;
    background: var(--blue); padding: 3px 8px; margin-right: auto;
  }
  .nav-menu { display: flex; gap: 17px; list-style: none; }
  .nav-menu li { font-size: 5.5px; color: #fff; letter-spacing: .05em; }
  .nav-menu .nav-contact { border: 1px solid #fff; padding: 2px 5px; }
  .hero-frame {
    position: absolute; left: 163px; top: 48px; width: 178px; height: 205px;
    border: 1.5px solid rgba(255,255,255,.9);
  }
  .hero-title {
    position: absolute; left: 163px; top: 74px; width: 178px;
    font-family: "Parisienne", cursive; font-size: 29px; line-height: 48px; font-weight: 400;
    color: #fff; text-align: center; text-shadow: 0 1px 4px rgba(0,0,0,.25);
  }
  .hero-company {
    position: absolute; right: 18px; top: 286px;
    font-family: "Cormorant Garamond", serif; font-size: 11px; color: #fff; letter-spacing: .08em;
  }

  /* lead */
  .lead { position: absolute; left: 0; top: 326px; width: 521px; text-align: center; }
  .lead-title {
    font-family: "Noto Serif JP", serif; font-size: 11px; font-weight: 500;
    color: var(--navy); letter-spacing: .06em;
  }
  .lead-title::after {
    content: ""; display: block; width: 200px; height: 1px; margin: 6px auto 6px;
    background: var(--line);
  }
  .lead-text { font-size: 6px; line-height: 10px; color: var(--muted); }

  /* service collage */
  .services { position: absolute; left: 42px; top: 400px; width: 439px; height: 240px; }
  .photo { position: absolute; }
  .photo-a { left: 0; top: 0; width: 215px; height: 110px;
    background: linear-gradient(160deg, #7fb0dc, #4b7fa9 60%, #2f5470); }
  .photo-b { left: 217px; top: 0; width: 222px; height: 110px;
    background: linear-gradient(170deg, #9ec4e6, #5b87b4 50%, #6c7e8f); }
  .photo-c { left: 0; top: 112px; width: 215px; height: 128px;
    background: linear-gradient(180deg, #a7cbe9, #6a91b5 45%, #8a9aa8 75%, #52606c); }
  .photo-d { left: 217px; top: 112px; width: 222px; height: 128px;
    background: linear-gradient(175deg, #8fbbe0, #6f8fae 50%, #4e5d6b); }
  .service-badge {
    position: absolute; width: 64px; height: 64px; border-radius: 50%;
    border: 1.5px solid #fff; background: rgba(29,41,66,.35);
    display: flex; align-items: center; justify-content: center; text-align: center;
    color: #fff; font-size: 6.5px; line-height: 10px; letter-spacing: .05em;
  }
  .badge-1 { left: 160px; top: 24px; }
  .badge-2 { left: 300px; top: 18px; }
  .badge-3 { left: 160px; top: 144px; }

  /* information */
  .info { position: absolute; left: 60px; top: 665px; width: 400px; }
  .info-head { display: flex; align-items: baseline; gap: 8px;
    border-bottom: 1px solid var(--line); padding-bottom: 4px; }
  .info-title { font-family: "Cormorant Garamond", serif; font-size: 13px; font-weight: 500;
    color: var(--navy); letter-spacing: .12em; }
  .info-sub { font-size: 5.5px; color: var(--muted); }
  .info-list { list-style: none; margin-top: 9px; }
  .info-list li { display: flex; gap: 14px; font-size: 5.5px; line-height: 9px;
    color: var(--ink); padding: 4px 0; border-bottom: 1px dotted var(--line); }
  .info-date { color: var(--blue); width: 34px; flex: none; }

  /* contact */
  .contact { position: absolute; left: 56px; top: 778px; width: 408px; height: 182px; }
  .contact-photo { position: absolute; left: 0; top: 0; width: 258px; height: 182px;
    background: linear-gradient(180deg, #b9d4ec 0%, #d7e5f1 35%, #a4a9ad 60%, #6f7478 85%, #55595c); }
  .contact-panel { position: absolute; left: 258px; top: 0; width: 150px; height: 182px;
    background: var(--navy); color: #fff; padding: 26px 0 0 22px; }
  .contact-title { font-family: "Cormorant Garamond", serif; font-size: 13px; letter-spacing: .12em; }
  .contact-sub { font-size: 5.5px; opacity: .8; margin: 2px 0 20px; }
  .contact-tel { display: flex; align-items: center; gap: 5px; font-size: 9px;
    font-weight: 500; margin-bottom: 7px; letter-spacing: .04em; }
  .contact-form { display: inline-flex; align-items: center; gap: 5px; margin-top: 12px;
    border: 1px solid #fff; font-size: 6.5px; padding: 5px 12px; }

  /* footer */
  .footer { position: absolute; left: 0; top: 992px; width: 521px; height: 208px;
    background: linear-gradient(180deg, #7ea9d1 0%, #5c7fa4 40%, #3a4e69 75%, #27354c 100%); }
  .footer-shade { position: absolute; left: 0; top: 0; width: 521px; height: 208px;
    background: rgba(29,41,66,.35); }
  .footer-info { position: absolute; left: 28px; top: 60px; color: #fff; }
  .footer-name { font-family: "Cormorant Garamond", serif; font-size: 9px; letter-spacing: .08em; margin-bottom: 5px; }
  .footer-addr { font-size: 5.5px; line-height: 9px; opacity: .9; }
  .footer-copy { position: absolute; left: 0; bottom: 8px; width: 521px; text-align: center;
    font-size: 5px; color: rgba(255,255,255,.75); letter-spacing: .05em; }
</style>
</head>
<body>
  <svg class="band" viewBox="0 0 801 1200" aria-hidden="true">
    <polygon points="0,610 801,520 801,660 0,760" fill="var(--band)"/>
  </svg>

  <div class="page">
    <div class="page-bg"></div>

    <header class="hero" role="img" aria-label="晴れた空の下の海辺の高層ビル街とヤシの木の眺め">
      <nav class="nav">
        <span class="nav-brand">Aoshio</span>
        <ul class="nav-menu">
          <li>HOME</li><li>COMPANY</li><li>SERVICE</li><li>RECRUIT</li><li class="nav-contact">CONTACT</li>
        </ul>
      </nav>
      <div class="hero-frame"></div>
      <h1 class="hero-title">Safety<br>and<br>High Quality</h1>
      <p class="hero-company">〇〇〇〇〇〇〇〇Company Limited</p>
    </header>

    <section class="lead">
      <h2 class="lead-title">より一層安全・安心な高品質サービスの実現へ</h2>
      <p class="lead-text">〇〇〇〇〇〇は「Safety ＆ High Quality」をモットーに、<br>お客様の大切な時間を守り、安心して過ごせる移動サービスをご提供しております。</p>
    </section>

    <section class="services">
      <div class="photo photo-a" role="img" aria-label="海辺の街並みの空撮"></div>
      <div class="photo photo-b" role="img" aria-label="空港に並ぶ旅客機"></div>
      <div class="photo photo-c" role="img" aria-label="ヤシの木の並ぶ道に停まる観光バス"></div>
      <div class="photo photo-d" role="img" aria-label="車両が並ぶ整備場"></div>
      <div class="service-badge badge-1">観光案内<br>TOUR</div>
      <div class="service-badge badge-2">空港送迎<br>AIRPORT</div>
      <div class="service-badge badge-3">貸切バス<br>CHARTER</div>
    </section>

    <section class="info">
      <div class="info-head">
        <h2 class="info-title">INFORMATION</h2>
        <span class="info-sub">お知らせ・新着情報</span>
      </div>
      <ul class="info-list">
        <li><span class="info-date">2019.04.01</span><span>新年度の営業体制についてお知らせいたします。詳細は各ページをご確認ください。<br>春の観光シーズンに向けた特別プランのご予約受付を開始いたしました。</span></li>
        <li><span class="info-date">2019.03.15</span><span>ホームページをリニューアルいたしました。</span></li>
      </ul>
    </section>

    <section class="contact">
      <div class="contact-photo" role="img" aria-label="晴天の下の駅前の街並み"></div>
      <div class="contact-panel">
        <h2 class="contact-title">CONTACT</h2>
        <p class="contact-sub">お問い合わせ</p>
        <p class="contact-tel">
          <svg width="9" height="9" viewBox="0 0 24 24" aria-hidden="true"><path fill="#fff" d="M6.6 10.8a15.1 15.1 0 006.6 6.6l2.2-2.2c.3-.3.7-.4 1-.2 1.1.4 2.3.6 3.6.6.6 0 1 .4 1 1V20c0 .6-.4 1-1 1C10.6 21 3 13.4 3 4c0-.6.4-1 1-1h3.5c.6 0 1 .4 1 1 0 1.3.2 2.5.6 3.6.1.3 0 .7-.2 1z"/></svg>
          03-5550-0142
        </p>
        <p class="contact-tel">
          <svg width="9" height="9" viewBox="0 0 24 24" aria-hidden="true"><path fill="#fff" d="M6.6 10.8a15.1 15.1 0 006.6 6.6l2.2-2.2c.3-.3.7-.4 1-.2 1.1.4 2.3.6 3.6.6.6 0 1 .4 1 1V20c0 .6-.4 1-1 1C10.6 21 3 13.4 3 4c0-.6.4-1 1-1h3.5c.6 0 1 .4 1 1 0 1.3.2 2.5.6 3.6.1.3 0 .7-.2 1z"/></svg>
          03-5550-0198
        </p>
        <span class="contact-form">
          <svg width="9" height="7" viewBox="0 0 18 14" aria-hidden="true"><rect x="1" y="1" width="16" height="12" fill="none" stroke="#fff" stroke-width="1.5"/><polyline points="1,1 9,8 17,1" fill="none" stroke="#fff" stroke-width="1.5"/></svg>
          Mail Form
        </span>
      </div>
    </section>

    <footer class="footer" role="img" aria-label="夕暮れの都市の高層ビル群">
      <div class="footer-shade"></div>
      <div class="footer-info">
        <p class="footer-name">〇〇〇〇〇〇〇〇Company Limited</p>
        <p class="footer-addr">〒000-0000 〇〇県〇〇市〇〇町0-0-0<br>TEL 03-5550-0142 / FAX 03-5550-0198</p>
      </div>
      <p class="footer-copy">© 〇〇〇〇〇〇 Company Limited. All Rights Reserved.</p>
    </footer>
  </div>
</body>
</html>
```